Business Card Design Project

We need a business card design for a consultancy called 'Amber Ridge'. The design should communicate innovation and professionalism. The colors used should complement our logo. Please include source files for winning design.
Updates

Industry/Entity Type

Business

Colors

Designer to choose colors to be used in the design.

Requirements
Must have
• Card size should be 85mm x 50mm. The back side of the card should be the logo on a black background. The front side should display the name 'Amber Ridge' along with standard information. The front's design should graphically complement the back.
Nice to have
• Any graphical elements in the front the complement the back side (with the logo on a black background) would be a plus.

```html
<!DOCTYPE html>
<html lang="en">
<head>
<meta charset="utf-8">
<title>Amber Ridge Business Card</title>
<link href="https://fonts.googleapis.com/css2?family=Cinzel:wght@500&display=swap" rel="stylesheet">
<style>
  :root {
    --stage: #808080;
    --stage-edge: #4a4a4a;
    --slate: #414549;
    --amber: #f58e1f;
    --amber-light: #f7a03a;
    --gold: #f2be74;
    --ink: #111111;
    --muted: #4a4d52;
  }
  * { margin: 0; padding: 0; box-sizing: border-box; }
  html, body { width: 1200px; height: 901px; overflow: hidden; }
  body {
    background: var(--stage);
    border: 2px solid var(--stage-edge);
    position: relative;
    font-family: Arial, Helvetica, sans-serif;
  }
  .card {
    position: absolute;
    left: 287px;
    width: 626px;
    height: 368px;
    overflow: hidden;
  }
  .card-back { top: 42px; background: var(--slate); }
  .card-front { top: 490px; height: 367px; background: var(--amber); }

  .brand-mark {
    position: absolute;
    border-radius: 50%;
    background: var(--amber-light);
  }
  .brand-name {
    position: absolute;
    left: 0; right: 0;
    text-align: center;
    font-family: "Cinzel", Georgia, serif;
    font-weight: 500;
    color: var(--gold);
    white-space: nowrap;
  }
  .card-back .brand-mark { left: 216px; top: 68px; width: 194px; height: 194px; }
  .card-back .brand-name { top: 258px; font-size: 42px; letter-spacing: 1px; }

  .side-panel {
    position: absolute;
    left: 0; top: 0;
    width: 131px; height: 100%;
    background: var(--slate);
  }
  .side-bulge {
    position: absolute;
    left: -13px; top: 99px;
    width: 169px; height: 169px;
    border-radius: 50%;
    background: var(--slate);
  }
  .side-logo { position: absolute; left: 0; top: 0; width: 160px; height: 100%; }
  .side-logo .brand-mark { left: 31px; top: 135px; width: 80px; height: 80px; }
  .side-logo .brand-name { left: 0; width: 142px; top: 214px; font-size: 17px; }

  .contact { position: absolute; left: 164px; top: 0; color: var(--ink); }
  .contact p { position: absolute; left: 0; white-space: nowrap; font-size: 13px; }
  .contact .profession { top: 84px; font-size: 22px; color: var(--muted); }
  .contact .address { top: 141px; }
  .contact .phone { top: 199px; }
  .contact .email { top: 249px; }
  .contact .web { top: 295px; }
</style>
</head>
<body>
  <section class="card card-back">
    <div class="brand-mark"></div>
    <div class="brand-name">Amber Ridge</div>
  </section>

  <section class="card card-front">
    <div class="side-panel"></div>
    <div class="side-bulge"></div>
    <div class="side-logo">
      <div class="brand-mark"></div>
      <div class="brand-name">Amber Ridge</div>
    </div>
    <div class="contact">
      <p class="profession">Your profession</p>
      <p class="address">YOUR ADDRESS</p>
      <p class="phone">Phone</p>
      <p class="email">company@mail.com</p>
      <p class="web">www.companyname.com</p>
    </div>
  </section>
</body>
</html>
```